Book cover for book titled The Weary Sailor's Drop Ledger

Need a book cover for a book size 5.25 x 8.
Title: The Weary Sailor's Drop Ledger
Subtitle: 35 Habits Worth Shedding So You Can Build Calmer Days Through a Season of Change
Author: Dr. Harold P. Wingate
Foreword by Lionel Ashworth, Ph.D.
The book cover should be white. I have uploaded 2 photos. The closeup with the hat should go on the front with the text. The one in the chair should go on the back. It will be the only thing on the back.

```html
<!DOCTYPE html>
<html lang="en">
<head>
<meta charset="utf-8">
<title>The Weary Sailor's Drop Ledger — Book Cover</title>
<link href="https://fonts.googleapis.com/css2?family=Arimo:wght@400;700&family=Open+Sans:wght@400&family=Fira+Sans:ital,wght@0,700;1,300&display=swap" rel="stylesheet">
<style>
  :root {
    --page-bg: #e6e6e6;
    --cover-white: #ffffff;
    --ink: #0a0a0a;
    --accent-red: #cc1722;
    --photo-dark: #1c1d26;
    --photo-mid: #6f6a63;
    --photo-light: #d9cdb4;
  }
  * { box-sizing: border-box; margin: 0; padding: 0; }
  html, body {
    width: 1200px; height: 853px; overflow: hidden;
    background: var(--page-bg);
  }
  .stage { position: relative; width: 1200px; height: 853px; }

  .cover {
    position: absolute; top: 156px;
    width: 389px; height: 594px;
    background: var(--cover-white);
    overflow: hidden;
  }
  .cover--front { left: 197px; }
  .cover--back { left: 638px; }

  /* Front cover */
  .title {
    position: absolute; left: 73px; top: 24px;
    font-family: "Arimo", Arial, sans-serif;
    font-weight: 700; font-size: 50px; line-height: 45px;
    letter-spacing: -1px; color: var(--ink);
  }
  .title span { display: block; }
  .title .title__accent {
    color: var(--accent-red); font-weight: 400; letter-spacing: -2px;
  }

  .portrait-frame {
    position: absolute; left: 84px; top: 212px;
    width: 234px; height: 305px;
    border: 3px solid var(--ink);
    padding: 4px;
    background: var(--cover-white);
  }
  .portrait-frame__inner {
    position: relative; width: 100%; height: 100%;
    border: 2px solid var(--accent-red);
  }
  .portrait {
    position: absolute; inset: 1px;
    background: linear-gradient(180deg, var(--cover-white) 0%, var(--photo-light) 18%, #c8b99c 30%, var(--photo-mid) 50%, #3a3a44 68%, var(--photo-dark) 82%);
  }
  .subtitle {
    position: absolute; left: 8px; right: 8px; bottom: 8px;
    font-family: "Open Sans", sans-serif;
    font-size: 12.5px; line-height: 17px;
    color: var(--cover-white); text-align: center;
  }

  .credit-band {
    position: absolute; left: 0; top: 526px;
    width: 100%; height: 59px;
    background: var(--accent-red);
    padding: 12px 0 0 77px;
    font-family: "Fira Sans", sans-serif;
    font-size: 12.5px; line-height: 16.5px;
    color: var(--cover-white);
  }
  .credit-band .label { font-style: italic; font-weight: 300; }
  .credit-band .name { font-weight: 700; letter-spacing: 0.4px; }

  /* Back cover */
  .band { position: absolute; left: 0; width: 100%; height: 59px; background: var(--accent-red); }
  .band--top { top: 19px; }
  .band--bottom { top: 517px; }
  .seated-photo {
    position: absolute; left: 85px; top: 149px;
    width: 272px; height: 332px;
    background: radial-gradient(ellipse at 50% 40%, #2a2c3a 0%, #3c4a6a 35%, #ece8e0 62%, var(--cover-white) 80%);
  }
</style>
</head>
<body>
<main class="stage">
  <section class="cover cover--front" aria-label="Front cover">
    <h1 class="title">
      <span>The</span>
      <span>Weary</span>
      <span>Sailor's</span>
      <span class="title__accent">Drop Ledger</span>
    </h1>

    <div class="portrait-frame">
      <div class="portrait-frame__inner">
        <div class="portrait" role="img" aria-label="Close-up photo of the author in a straw boater hat, glasses and face mask"></div>
        <p class="subtitle">35 Habits Worth Shedding So You Can Build Calmer Days Through a Season of Change</p>
      </div>
    </div>

    <div class="credit-band">
      <p><span class="label">Author</span>: <span class="name">Dr. Harold P. Wingate</span></p>
      <p><span class="label">Foreword</span> <span class="name">by Lionel Ashworth, Ph.D.</span></p>
    </div>
  </section>

  <section class="cover cover--back" aria-label="Back cover">
    <div class="band band--top"></div>
    <div class="seated-photo" role="img" aria-label="Photo of the author seated in a white armchair, wearing jeans and red sneakers, hat beside his foot"></div>
    <div class="band band--bottom"></div>
  </section>
</main>
</body>
</html>
```